Velisa Seafood Shipping Packaging Re-Design

We need a packaging (Shipping Carton) design for our Seafood Products (FROZEN). We already have a basic packaging design which we prefer to have a modern touch on it.
Spec :
1. It must show our logo (Attached), note that the text of "VELISA" which accompany the logo is optional, it can be omitted & showing only the logo.
2. Main color is Blue
3. Our carton is regular shipping box with dimension L43cm x W 27cm x H 16cm.
4. Our material of Carton is both Brown & White Kraft Paperboard, so the design should look nice in both material.

Attached our Logo and packaging design.

Target Market(s)

Frozen Seafood Distributor & Seafood Buyer

Industry/Entity Type

Food Production

Requirements
Must have
• 1. Must Show our Logo
• 2. Main Color of the Text/Logo is Blue
• 3. On the side of the packaging / Carton must show two box of CODE & SIZE
• 4. Must Show these icons :
• a. Handle with Care
• b. Maximum Stackable 10 Carton
• c. Recyleable Material
• d. Protect from the Water/Rain
Nice to have
• Would prefer to have a modern design

```html
<!DOCTYPE html>
<html lang="en">
<head>
<meta charset="utf-8">
<title>Velisa Frozen Seafood Shipping Carton – Dielines</title>
<link href="https://fonts.googleapis.com/css2?family=Cinzel:wght@500&family=Exo+2:wght@700&display=swap" rel="stylesheet">
<style>
  :root{
    --page:#ffffff;
    --cut:#c7c9e6;
    --navy:#14285e;
    --blue:#3f7fc0;
    --blue-light:#7fb0dc;
    --board:#ffffff;
    --wave:#4f8fcf;
    --wave-soft:#9cc3e6;
    --mark:#3c6ea8;
  }
  *{box-sizing:border-box;margin:0;padding:0}
  html,body{width:960px;height:1200px;overflow:hidden;background:var(--page)}
  .canvas{position:relative;width:960px;height:1200px}
  .dieline{position:absolute;left:39px;width:882px;height:264px}
  .dieline--white{top:300px}
  .dieline--kraft{top:660px;
    --board:#d2ab80;--wave:#4d7f86;--wave-soft:#7ea4a3;--mark:#2f5d6e;--cut:#b89066}
  .panel{position:absolute;background:var(--board);border:1px solid var(--cut);overflow:hidden}
  .glue-flap{position:absolute;left:0;top:83px;width:23px;height:98px}
  .glue-flap polygon{fill:var(--board);stroke:var(--cut);stroke-width:1}
  .wave-band{position:absolute;left:0;top:0;width:100%;height:24px}
  .temp-pill{position:absolute;left:50%;transform:translateX(-50%);background:var(--navy);color:#fff;
    font:700 10px/1 "Exo 2",sans-serif;padding:3px 9px;border-radius:9px;white-space:nowrap;display:flex;gap:4px;align-items:center}
  .label-pair{position:absolute;display:flex;justify-content:space-between}
  .label-box{border:1.2px solid var(--navy);border-radius:5px;overflow:hidden;background:transparent}
  .label-box__title{background:var(--navy);color:#fff;font:700 8.5px/1 "Exo 2",sans-serif;text-align:center;padding:3px 0;letter-spacing:.3px}
  .brand{position:absolute;left:50%;transform:translateX(-50%);display:flex;flex-direction:column;align-items:center}
  .brand__dot{width:36px;height:36px;border-radius:50%;background:var(--mark)}
  .brand__name{font:500 21px/1 "Cinzel",serif;color:var(--navy);letter-spacing:1px;margin-top:4px}
  .brand--inverted{transform:translateX(-50%) rotate(180deg)}
  .base-waves{position:absolute;left:0;bottom:0;width:100%;height:22px}
  .care-icons{position:absolute;left:0;width:100%;display:flex;justify-content:center;gap:10px}
  .care-icons svg{width:17px;height:17px}
</style>
</head>
<body>
<svg width="0" height="0" style="position:absolute" aria-hidden="true">
  <defs>
    <symbol id="band" viewBox="0 0 264 24" preserveAspectRatio="none">
      <path d="M0 0H264V16C220 10 180 22 132 16C84 10 44 22 0 15Z" fill="var(--wave)" opacity=".85"/>
      <path d="M0 6C50 10 90 2 140 7C190 12 230 4 264 7" stroke="var(--wave-soft)" stroke-width="2" fill="none"/>
    </symbol>
    <symbol id="baseWaves" viewBox="0 0 264 22" preserveAspectRatio="none">
      <path d="M14 14C70 4 120 8 170 10C210 12 235 9 250 7" stroke="var(--wave)" stroke-width="3" fill="none"/>
      <path d="M20 18C80 10 140 14 190 15C220 16 240 14 252 12" stroke="var(--wave-soft)" stroke-width="2" fill="none"/>
    </symbol>
    <symbol id="flake" viewBox="0 0 10 10"><path d="M5 0V10M0 5H10M1.5 1.5L8.5 8.5M8.5 1.5L1.5 8.5" stroke="#fff" stroke-width="1.3"/></symbol>
    <symbol id="iconRain" viewBox="0 0 20 20"><circle cx="10" cy="10" r="9" fill="none" stroke="var(--navy)" stroke-width="1.2"/><path d="M4.5 10a5.5 4.5 0 0 1 11 0Z" fill="var(--navy)"/><path d="M10 10v4a1.5 1.5 0 0 1-3 0" fill="none" stroke="var(--navy)" stroke-width="1.2"/></symbol>
    <symbol id="iconCare" viewBox="0 0 20 20"><circle cx="10" cy="10" r="9" fill="none" stroke="var(--navy)" stroke-width="1.2"/><rect x="7" y="5" width="6" height="5" fill="var(--navy)"/><path d="M4.5 9.5L7.5 14H12.5L15.5 9.5" fill="none" stroke="var(--navy)" stroke-width="1.4"/></symbol>
    <symbol id="iconStack" viewBox="0 0 20 20"><circle cx="10" cy="10" r="9" fill="none" stroke="var(--navy)" stroke-width="1.2"/><text x="10" y="10.5" text-anchor="middle" font-family="Exo 2, sans-serif" font-weight="700" font-size="6.5" fill="var(--navy)">10</text><path d="M6 12.5H14M6 14.5H14" stroke="var(--navy)" stroke-width="1"/></symbol>
    <symbol id="iconRecycle" viewBox="0 0 20 20"><circle cx="10" cy="10" r="9" fill="none" stroke="var(--navy)" stroke-width="1.2"/><path d="M10 5L13.5 11H6.5Z M8 13.5H12" fill="none" stroke="var(--navy)" stroke-width="1.4" stroke-linejoin="round"/></symbol>
  </defs>
</svg>

<main class="canvas">
  <!-- White kraft board -->
  <section class="dieline dieline--white" aria-label="Carton dieline on white board">
    <svg class="glue-flap" viewBox="0 0 23 98"><polygon points="22,0 0,8 0,90 22,98"/></svg>

    <div class="panel" style="left:22px;top:0;width:264px;height:83px">
      <svg class="wave-band"><use href="#band"/></svg>
      <div class="temp-pill" style="top:10px"><svg width="9" height="9"><use href="#flake"/></svg>-18℃</div>
      <div class="label-pair" style="left:36px;right:36px;top:31px">
        <div class="label-box" style="width:87px;height:47px"><div class="label-box__title">CODE 代码</div></div>
        <div class="label-box" style="width:87px;height:47px"><div class="label-box__title">SIZE 规格</div></div>
      </div>
    </div>
    <div class="panel" style="left:286px;top:0;width:166px;height:83px"></div>
    <div class="panel" style="left:452px;top:0;width:264px;height:83px">
      <svg class="wave-band"><use href="#band"/></svg>
      <div class="brand brand--inverted" style="top:24px;flex-direction:row;gap:8px;align-items:center"><span class="brand__dot" style="width:30px;height:30px"></span><span class="brand__name" style="margin:0;font-size:17px">VELISA</span></div>
    </div>
    <div class="panel" style="left:716px;top:0;width:166px;height:83px"></div>

    <div class="panel" style="left:22px;top:83px;width:264px;height:98px">
      <div class="brand" style="top:6px"><span class="brand__dot"></span><span class="brand__name">VELISA</span></div>
      <svg class="base-waves"><use href="#baseWaves"/></svg>
    </div>
    <div class="panel" style="left:286px;top:83px;width:166px;height:98px">
      <div class="temp-pill" style="top:6px"><svg width="9" height="9"><use href="#flake"/></svg>-18℃</div>
      <div class="label-pair" style="left:11px;right:11px;top:24px">
        <div class="label-box" style="width:67px;height:49px"><div class="label-box__title">CODE 代码</div></div>
        <div class="label-box" style="width:67px;height:49px"><div class="label-box__title">SIZE 规格</div></div>
      </div>
      <div class="care-icons" style="top:77px"><svg><use href="#iconRain"/></svg><svg><use href="#iconCare"/></svg><svg><use href="#iconStack"/></svg><svg><use href="#iconRecycle"/></svg></div>
    </div>
    <div class="panel" style="left:452px;top:83px;width:264px;height:98px">
      <div class="brand" style="top:6px"><span class="brand__dot"></span><span class="brand__name">VELISA</span></div>
      <svg class="base-waves"><use href="#baseWaves"/></svg>
    </div>
    <div class="panel" style="left:716px;top:83px;width:166px;height:98px">
      <div class="temp-pill" style="top:6px"><svg width="9" height="9"><use href="#flake"/></svg>-18℃</div>
      <div class="label-pair" style="left:11px;right:11px;top:24px">
        <div class="label-box" style="width:67px;height:49px"><div class="label-box__title">CODE 代码</div></div>
        <div class="label-box" style="width:67px;height:49px"><div class="label-box__title">SIZE 规格</div></div>
      </div>
      <div class="care-icons" style="top:77px"><svg><use href="#iconRain"/></svg><svg><use href="#iconCare"/></svg><svg><use href="#iconStack"/></svg><svg><use href="#iconRecycle"/></svg></div>
    </div>

    <div class="panel" style="left:22px;top:181px;width:264px;height:83px"></div>
    <div class="panel" style="left:286px;top:181px;width:166px;height:83px"></div>
    <div class="panel" style="left:452px;top:181px;width:264px;height:83px"></div>
    <div class="panel" style="left:716px;top:181px;width:166px;height:83px"></div>
  </section>

  <!-- Brown kraft board -->
  <section class="dieline dieline--kraft" aria-label="Carton dieline on brown kraft board">
    <svg class="glue-flap" viewBox="0 0 23 98"><polygon points="22,0 0,8 0,90 22,98"/></svg>

    <div class="panel" style="left:22px;top:0;width:264px;height:83px">
      <svg class="wave-band"><use href="#band"/></svg>
      <div class="temp-pill" style="top:10px"><svg width="9" height="9"><use href="#flake"/></svg>-18℃</div>
      <div class="label-pair" style="left:36px;right:36px;top:31px">
        <div class="label-box" style="width:87px;height:47px"><div class="label-box__title">CODE 代码</div></div>
        <div class="label-box" style="width:87px;height:47px"><div class="label-box__title">SIZE 规格</div></div>
      </div>
    </div>
    <div class="panel" style="left:286px;top:0;width:166px;height:83px"></div>
    <div class="panel" style="left:452px;top:0;width:264px;height:83px">
      <svg class="wave-band"><use href="#band"/></svg>
      <div class="brand brand--inverted" style="top:24px;flex-direction:row;gap:8px;align-items:center"><span class="brand__dot" style="width:30px;height:30px"></span><span class="brand__name" style="margin:0;font-size:17px">VELISA</span></div>
    </div>
    <div class="panel" style="left:716px;top:0;width:166px;height:83px"></div>

    <div class="panel" style="left:22px;top:83px;width:264px;height:98px">
      <div class="brand" style="top:6px"><span class="brand__dot"></span><span class="brand__name">VELISA</span></div>
      <svg class="base-waves"><use href="#baseWaves"/></svg>
    </div>
    <div class="panel" style="left:286px;top:83px;width:166px;height:98px">
      <div class="temp-pill" style="top:6px"><svg width="9" height="9"><use href="#flake"/></svg>-18℃</div>
      <div class="label-pair" style="left:11px;right:11px;top:24px">
        <div class="label-box" style="width:67px;height:49px"><div class="label-box__title">CODE 代码</div></div>
        <div class="label-box" style="width:67px;height:49px"><div class="label-box__title">SIZE 规格</div></div>
      </div>
      <div class="care-icons" style="top:77px"><svg><use href="#iconRain"/></svg><svg><use href="#iconCare"/></svg><svg><use href="#iconStack"/></svg><svg><use href="#iconRecycle"/></svg></div>
    </div>
    <div class="panel" style="left:452px;top:83px;width:264px;height:98px">
      <div class="brand" style="top:6px"><span class="brand__dot"></span><span class="brand__name">VELISA</span></div>
      <svg class="base-waves"><use href="#baseWaves"/></svg>
    </div>
    <div class="panel" style="left:716px;top:83px;width:166px;height:98px">
      <div class="temp-pill" style="top:6px"><svg width="9" height="9"><use href="#flake"/></svg>-18℃</div>
      <div class="label-pair" style="left:11px;right:11px;top:24px">
        <div class="label-box" style="width:67px;height:49px"><div class="label-box__title">CODE 代码</div></div>
        <div class="label-box" style="width:67px;height:49px"><div class="label-box__title">SIZE 规格</div></div>
      </div>
      <div class="care-icons" style="top:77px"><svg><use href="#iconRain"/></svg><svg><use href="#iconCare"/></svg><svg><use href="#iconStack"/></svg><svg><use href="#iconRecycle"/></svg></div>
    </div>

    <div class="panel" style="left:22px;top:181px;width:264px;height:83px"></div>
    <div class="panel" style="left:286px;top:181px;width:166px;height:83px"></div>
    <div class="panel" style="left:452px;top:181px;width:264px;height:83px"></div>
    <div class="panel" style="left:716px;top:181px;width:166px;height:83px"></div>
  </section>
</main>
</body>
</html>
```